Quorvane Learning App for Children with Dyslexia

Project Description:

We are seeking a talented UI/UX designer to create engaging and intuitive designs for Quorvane, an innovative educational app designed to help children learn letters and words through a multisensory learning approach. The app aims to be particularly helpful for children with dyslexia, providing a supportive and interactive learning environment.

Key App Features & Design Requirements:

Account Creation Screen: Design a welcoming and straightforward sign-up page that allows users to register with their email or continue with Brindlewave. The design should be clean, focusing on user-friendliness and accessibility, adhering to our terms of service and privacy policy.

Main Screen Design: The main screen should allocate at least 4/6 of its height to the interactive drawing area. It needs to display word prompts in both correct and scrambled orders and include options to "Show all Words," "Play all words," and a search function. The interface should be vibrant, engaging, and easy to navigate for children.

Profile Section: Create a user-friendly profile page that allows users to edit their profile image, name, username, email, links, and bio. The design should be clean and encourage user engagement.

QuorTally Page: This section will display the user's learning progress, including rankings, a learning curve, and recently learned words. It should visually represent progress in a motivating and understandable way, suitable for a younger audience.

Visual and Auditory Feedback Implementation: Incorporate elements that support visual and auditory feedback, using dyslexia-friendly formats. This includes choosing appropriate colors, fonts, and auditory cues.

Accessibility and Customization Settings: Designs should include settings for adjusting visual contrast, font size, and the word list to accommodate individual preferences and needs.

Feel free to add more interactions and/or pages.

Design preferences:

Color Scheme: Use a bright, inviting color palette that stimulates learning and engagement without overwhelming the users.
Font Selection: Opt for fonts that are readable and accessible, particularly for users with dyslexia.
Icons and Graphics: Design custom icons and graphics that are cohesive with the app's theme and purpose. Illustrations should be simple, relatable, and supportive of the learning process.

Target Market(s)

Educational

Industry/Entity Type

Educational

Colors
0054AA
0677BA
7BADD7
CADEEF
E8F1F8
0094D4
00A9DD
6FCCEA
C7EBF8
E9F6FB

Requirements
Must have
• Educational app, a writing area, scoring and account management
Nice to have
• Statistics, Ranking Page, Settings and some nice visual features

```html
<!DOCTYPE html>
<html lang="en">
<head>
<meta charset="utf-8">
<title>Quorvane – App Screens</title>
<link href="https://fonts.googleapis.com/css2?family=Inter:wght@400;500;600;700&display=swap" rel="stylesheet">
<style>
:root{
  --stage:#5b5b5b;
  --blue-deep:#0054AA;
  --blue:#0677BA;
  --blue-sky:#0094D4;
  --blue-bright:#00A9DD;
  --blue-pale:#CADEEF;
  --blue-mist:#E8F1F8;
  --ink:#111;
  --muted:#555;
  --points:#f5dc12;
  --chip-apple:#0a4fa8;
  --chip-ball:#ff9a00;
  --chip-cat:#d62ff0;
  --chip-dog:#a6cb1e;
  --chip-eagle:#f0463f;
  --chip-food:#ff0e8a;
  --green:#3cc07a;
  --teal:#12a6cf;
}
*{box-sizing:border-box;margin:0;padding:0}
html,body{width:1200px;height:908px;overflow:hidden;background:#fff;font-family:"Inter",sans-serif}
.stage{position:absolute;left:0;top:0;width:1530px;height:1158px;transform:scale(.78431);transform-origin:0 0;background:var(--stage);border-radius:44px;overflow:hidden}
.blob{position:absolute;border-radius:50%}
.blob--top{left:-200px;top:-255px;width:590px;height:590px;background:var(--blue-sky)}
.blob--bottom{left:1135px;top:835px;width:530px;height:530px;background:#0563b4}
.screen{position:absolute;width:375px;border-radius:30px;overflow:hidden}
.abs{position:absolute}
.center{left:0;right:0;text-align:center}
/* signup */
.signup{left:163px;top:149px;height:812px;background:linear-gradient(180deg,#0a58b0 0%,#0a7ec8 55%,#08a2dc 100%);color:#fff}
.brand{top:96px;font-size:30px;font-weight:700}
.tagline{top:138px;font-size:14px}
.heading{top:236px;font-size:25px;font-weight:700}
.sub{top:278px;font-size:14px}
.field-label{left:24px;top:341px;font-size:12px}
.field-label span{color:#ff6b6b}
.input{left:24px;top:363px;width:327px;height:40px;background:#fff;border-radius:4px}
.btn-green{background:linear-gradient(180deg,var(--green),var(--teal));color:#fff;border-radius:6px;font-size:16px;font-weight:500;display:flex;align-items:center;justify-content:center}
.signup .btn-green{left:24px;top:427px;width:327px;height:40px}
.divider{left:24px;top:493px;width:327px;display:flex;align-items:center;gap:14px;font-size:11px}
.divider i{flex:1;height:1px;background:rgba(255,255,255,.6)}
.alt-btn{left:24px;top:535px;width:327px;height:44px;background:#e4f1fa;border-radius:6px;color:var(--ink);font-size:16px;font-weight:500;display:flex;align-items:center;justify-content:center;gap:8px}
.alt-btn b{width:14px;height:14px;border-radius:50%;background:var(--blue)}
.terms{top:661px;font-size:14px;line-height:28px;padding:0 20px}
.terms strong{font-weight:600}
/* shared */
.status{left:24px;right:24px;top:14px;display:flex;justify-content:space-between;font-size:15px;font-weight:600;color:#fff}
.tabbar{left:0;right:0;bottom:0;background:#fff;display:flex;justify-content:space-around;padding-top:14px}
.tab{width:80px;display:flex;flex-direction:column;align-items:center;gap:4px;font-size:12px;color:#222}
.tab.active{color:var(--blue-sky)}
.indicator{width:134px;height:4px;border-radius:2px;background:#111;left:121px}
/* main */
.main{left:578px;top:149px;height:860px;background:linear-gradient(180deg,#cfe2f2 0%,#e6f1f8 100%)}
.main .header{left:0;right:0;top:0;height:211px;background:linear-gradient(180deg,#0466b8,#0a86c8)}
.title{font-size:20px;font-weight:500;color:#fff}
.main .title{top:58px}
.points{right:24px;top:62px;font-size:14px;font-weight:600;color:var(--points)}
.menu{left:26px;top:62px}
.search{left:24px;top:96px;width:327px;height:40px;background:#f4f6f8;border-radius:3px;display:flex;align-items:center;gap:10px;padding-left:12px;font-size:14px;color:#666}
.canvas-frame{left:24px;top:160px;width:327px;height:269px;background:#222;padding:14px}
.canvas-mat{width:100%;height:100%;background:#fff;padding:8px}
.drawing{width:100%;height:100%;background:linear-gradient(180deg,#cfeaf8 0%,#bfe3f0 55%,#a7d77e 100%)}
.pill{background:#fff;border-radius:4px;font-size:14px;font-weight:500;color:#111;display:flex;align-items:center;justify-content:center;height:42px;width:156px;top:465px}
.chip{width:102px;height:46px;border-radius:8px;color:#fff;font-size:17px;font-weight:500;display:flex;align-items:center;justify-content:center;box-shadow:0 4px 0 rgba(0,0,0,.12)}
.main .btn-green{left:24px;top:680px;width:327px;height:40px}
.main .tabbar{height:93px}
.main .indicator{top:846px}
/* profile */
.profile{left:993px;top:149px;height:812px;background:linear-gradient(180deg,#cadeef 0%,#e4eff8 100%)}
.profile .header{left:0;right:0;top:0;height:109px;background:linear-gradient(180deg,#0466b8,#0a8ccc)}
.profile .title{left:60px;top:58px}
.back{left:28px;top:60px}
.avatar{left:143px;top:144px;width:90px;height:90px;border-radius:50%;background:radial-gradient(circle at 50% 40%,#d9b9a4 0%,#9a86b8 55%,#6d6aa6 100%)}
.edit{left:172px;top:216px;width:32px;height:32px;border-radius:50%;background:var(--blue);border:2px solid #fff;display:flex;align-items:center;justify-content:center}
.row{left:24px;right:24px;display:flex;gap:14px}
.row .ico{width:44px;height:44px;border-radius:50%;background:#fff;display:flex;align-items:center;justify-content:center;flex:none}
.row .txt{flex:1;padding-top:6px}
.row small{display:block;font-size:12px;color:var(--muted);margin-bottom:4px}
.row p{font-size:15px;color:#111;line-height:23px}
.row .chev{padding-top:14px}
.profile .tabbar{height:94px}
.profile .indicator{top:797px}
</style>
</head>
<body>
<div class="stage">
  <div class="blob blob--top"></div>
  <div class="blob blob--bottom"></div>

  <!-- Sign up -->
  <section class="screen signup">
    <div class="abs center brand">Quorvane</div>
    <div class="abs center tagline">Learn letters and words</div>
    <div class="abs center heading">Create an account</div>
    <div class="abs center sub">Enter your email to sign up for this app</div>
    <div class="abs field-label">Email Address <span>*</span></div>
    <div class="abs input"></div>
    <div class="abs btn-green">Sign up with email</div>
    <div class="abs divider"><i></i>or<i></i></div>
    <div class="abs alt-btn"><b></b>Continue With Brindlewave</div>
    <p class="abs center terms">By clicking continue, you agree to our <strong>Terms of Service</strong> and <strong>Privacy Policy</strong></p>
  </section>

  <!-- Main -->
  <section class="screen main">
    <div class="abs header"></div>
    <div class="abs status"><span>9:41</span><span>▂▄▆ ◠ ▭</span></div>
    <svg class="abs menu" width="20" height="14" viewBox="0 0 20 14"><path d="M1 1h18M1 7h18M1 13h18" stroke="#fff" stroke-width="1.8" stroke-linecap="round"/></svg>
    <div class="abs center title">Main Screen</div>
    <div class="abs points">16 Points</div>
    <div class="abs search"><svg width="16" height="16" viewBox="0 0 16 16"><circle cx="7" cy="7" r="5.5" fill="none" stroke="#666" stroke-width="1.5"/><path d="M11 11l4 4" stroke="#666" stroke-width="1.5"/></svg>Search</div>
    <div class="abs canvas-frame"><div class="canvas-mat"><div class="drawing" role="img" aria-label="Child's crayon drawing of a tree, two children, a rainbow and the sun"></div></div></div>
    <div class="abs pill" style="left:24px">Show all Words</div>
    <div class="abs pill" style="left:195px">Play all words</div>
    <div class="abs chip" style="left:24px;top:535px;background:var(--chip-apple)">Apple</div>
    <div class="abs chip" style="left:136px;top:535px;background:var(--chip-ball)">Ball</div>
    <div class="abs chip" style="left:249px;top:535px;background:var(--chip-cat)">Cat</div>
    <div class="abs chip" style="left:24px;top:599px;background:var(--chip-dog)">Dog</div>
    <div class="abs chip" style="left:136px;top:599px;background:var(--chip-eagle)">Eagle</div>
    <div class="abs chip" style="left:249px;top:599px;background:var(--chip-food)">Food</div>
    <div class="abs btn-green">Show me the results</div>
    <nav class="abs tabbar">
      <div class="tab active"><svg width="26" height="26" viewBox="0 0 26 26" fill="none" stroke="currentColor" stroke-width="1.8"><path d="M3 12L13 3l10 9v11H16v-7h-6v7H3z"/></svg>Home</div>
      <div class="tab"><svg width="30" height="26" viewBox="0 0 30 26" fill="none" stroke="currentColor" stroke-width="1.8"><circle cx="8" cy="17" r="6"/><circle cx="22" cy="17" r="6"/><path d="M5 12l3-9h4v10M25 12l-3-9h-4v10M12 13h6"/></svg>Search</div>
      <div class="tab"><svg width="30" height="26" viewBox="0 0 30 26" fill="none" stroke="currentColor" stroke-width="1.8"><path d="M8 2h14v7a7 7 0 01-14 0zM8 5H3c0 5 3 7 5 7M22 5h5c0 5-3 7-5 7M15 16v5M10 24h10"/></svg>QuorTally</div>
      <div class="tab"><svg width="28" height="28" viewBox="0 0 28 28" fill="none" stroke="currentColor" stroke-width="1.8"><circle cx="14" cy="14" r="12"/><circle cx="14" cy="11" r="4.5"/><path d="M6 22c2-4 5-5 8-5s6 1 8 5"/></svg>Profile</div>
    </nav>
    <div class="abs indicator"></div>
  </section>

  <!-- Profile -->
  <section class="screen profile">
    <div class="abs header"></div>
    <div class="abs status"><span>9:41</span><span>▂▄▆ ◠ ▭</span></div>
    <svg class="abs back" width="12" height="20" viewBox="0 0 12 20"><path d="M10 2L2 10l8 8" fill="none" stroke="#fff" stroke-width="2"/></svg>
    <div class="abs title">Profile</div>
    <div class="abs avatar" role="img" aria-label="Profile photo of the user"></div>
    <div class="abs edit"><svg width="14" height="14" viewBox="0 0 14 14"><path d="M2 12l1-3 7-7 2 2-7 7zM9 3l2 2" fill="none" stroke="#fff" stroke-width="1.4"/></svg></div>

    <div class="abs row" style="top:288px"><div class="ico"><svg width="18" height="18" viewBox="0 0 18 18" fill="none" stroke="#111" stroke-width="1.5"><circle cx="9" cy="6" r="3.5"/><path d="M2 17c1-4 4-5 7-5s6 1 7 5"/></svg></div><div class="txt"><small>Name</small><p>Mira Solberg</p></div><svg class="chev" width="10" height="32" viewBox="0 0 10 32"><path d="M2 10l6 6-6 6" fill="none" stroke="#333" stroke-width="1.6"/></svg></div>
    <div class="abs row" style="top:352px"><div class="ico"><svg width="18" height="18" viewBox="0 0 18 18" fill="none" stroke="#111" stroke-width="1.5"><circle cx="9" cy="9" r="7.5"/><circle cx="9" cy="8" r="2.5"/><path d="M4.5 14c1.5-2 3-2.5 4.5-2.5s3 .5 4.5 2.5"/></svg></div><div class="txt"><small>Username</small><p>@username</p></div><svg class="chev" width="10" height="32" viewBox="0 0 10 32"><path d="M2 10l6 6-6 6" fill="none" stroke="#333" stroke-width="1.6"/></svg></div>
    <div class="abs row" style="top:416px"><div class="ico"><svg width="18" height="18" viewBox="0 0 18 18" fill="none" stroke="#111" stroke-width="1.5"><rect x="2" y="4" width="14" height="10" rx="1"/><path d="M2 5l7 5 7-5"/></svg></div><div class="txt"><small>Email</small><p>name@mailbox.test</p></div><svg class="chev" width="10" height="32" viewBox="0 0 10 32"><path d="M2 10l6 6-6 6" fill="none" stroke="#333" stroke-width="1.6"/></svg></div>
    <div class="abs row" style="top:480px"><div class="ico" style="margin-top:0"><svg width="20" height="18" viewBox="0 0 20 18" fill="none" stroke="#111" stroke-width="1.5"><path d="M8 5H5a4 4 0 000 8h3M12 5h3a4 4 0 010 8h-3M6 9h8"/></svg></div><div class="txt" style="padding-top:0"><small>Links</small><p style="margin-top:10px">sitefolio.test<br>mypage.test<br>yourspot.test</p></div><svg class="chev" style="padding-top:0" width="10" height="22" viewBox="0 0 10 22"><path d="M2 4l6 6-6 6" fill="none" stroke="#333" stroke-width="1.6"/></svg></div>
    <div class="abs row" style="top:587px"><div class="ico"><svg width="18" height="18" viewBox="0 0 18 18" fill="none" stroke="#111" stroke-width="1.5"><path d="M2 3h14v9H8l-4 3v-3H2z"/><path d="M6 7.5h.01M9 7.5h.01M12 7.5h.01" stroke-linecap="round" stroke-width="2"/></svg></div><div class="txt" style="padding-top:0"><small>Bio</small><p style="margin-top:10px;line-height:20px">A work in progress with a<br>sprinkle of glitter</p></div><svg class="chev" style="padding-top:0" width="10" height="22" viewBox="0 0 10 22"><path d="M2 4l6 6-6 6" fill="none" stroke="#333" stroke-width="1.6"/></svg></div>

    <nav class="abs tabbar">
      <div class="tab"><svg width="26" height="26" viewBox="0 0 26 26" fill="none" stroke="currentColor" stroke-width="1.8"><path d="M3 12L13 3l10 9v11H16v-7h-6v7H3z"/></svg>Home</div>
      <div class="tab"><svg width="30" height="26" viewBox="0 0 30 26" fill="none" stroke="currentColor" stroke-width="1.8"><circle cx="8" cy="17" r="6"/><circle cx="22" cy="17" r="6"/><path d="M5 12l3-9h4v10M25 12l-3-9h-4v10M12 13h6"/></svg>Search</div>
      <div class="tab"><svg width="30" height="26" viewBox="0 0 30 26" fill="none" stroke="currentColor" stroke-width="1.8"><path d="M8 2h14v7a7 7 0 01-14 0zM8 5H3c0 5 3 7 5 7M22 5h5c0 5-3 7-5 7M15 16v5M10 24h10"/></svg>QuorTally</div>
      <div class="tab active"><svg width="28" height="28" viewBox="0 0 28 28" fill="none" stroke="currentColor" stroke-width="1.8"><circle cx="14" cy="14" r="12"/><circle cx="14" cy="11" r="4.5"/><path d="M6 22c2-4 5-5 8-5s6 1 8 5"/></svg>Profile</div>
    </nav>
    <div class="abs indicator"></div>
  </section>
</div>
</body>
</html>
```